Business Card Design Project 4 Construction Business

I am after a creative, but sleek and simple/ clean business card design. This design will form the basis of future items and might include a logo or simply a creative way to lay out the text of my company name 'kestrel ventures'
I like the simplicity of black and white however I would also be happy to see a splash of colour introduced somehow to give the text some interest and make it stand out.
I would like a double sided card.
I am young (ish!) and professional, offering construction and project management services, what I don't want is the traditional builders type card featuring a cheesy hammer/ saw image etc.
As the company name, kestrel ventures, suggests, we focus on working closely and collaboratively together, in synergy with all stakeholders involved in the projects that we undertake
Construction

```html
<!DOCTYPE html>
<html lang="en">
<head>
<meta charset="utf-8">
<title>Kestrel Ventures — Business Card</title>
<link href="https://fonts.googleapis.com/css2?family=Michroma&display=swap" rel="stylesheet">
<style>
  :root {
    --backdrop: #2a2a2a;
    --card: #6a6a6a;
    --silver: #e4e4e4;
    --text: #f2f2f2;
    --accent: #e0262b;
  }
  * { margin: 0; padding: 0; box-sizing: border-box; }
  html, body {
    width: 1067px;
    height: 1200px;
    overflow: hidden;
    background: var(--backdrop);
    font-family: "Michroma", sans-serif;
  }
  .sheet {
    width: 1067px;
    height: 1200px;
    display: flex;
    flex-direction: column;
    align-items: center;
    justify-content: center;
    gap: 70px;
  }
  .card {
    position: relative;
    width: 760px;
    height: 434px;
    background: var(--card);
    box-shadow: 0 14px 30px rgba(0, 0, 0, 0.45);
  }
  .wordmark {
    color: var(--silver);
    font-size: 40px;
    letter-spacing: 1px;
    line-height: 1;
    white-space: nowrap;
  }
  .card-front .brand {
    position: absolute;
    right: 46px;
    bottom: 72px;
    text-align: right;
  }
  .card-front .website {
    margin-top: 18px;
    color: var(--text);
    font-size: 14px;
    letter-spacing: 1.5px;
    text-transform: uppercase;
  }
  .card-back .wordmark {
    position: absolute;
    left: 56px;
    top: 90px;
  }
  .contact {
    position: absolute;
    left: 90px;
    top: 225px;
    color: var(--text);
    font-size: 13px;
    letter-spacing: 1px;
    text-transform: uppercase;
  }
  .contact .person-name {
    color: var(--accent);
    font-size: 17px;
    letter-spacing: 1.5px;
  }
  .contact .person-role { margin-bottom: 20px; }
  .contact .address { margin-bottom: 8px; }
  .contact-line {
    display: flex;
    align-items: center;
    gap: 8px;
    line-height: 1.6;
  }
  .contact-line svg { width: 12px; height: 12px; fill: var(--accent); flex: none; }
</style>
</head>
<body>
<main class="sheet">
  <section class="card card-front" aria-label="Card front">
    <div class="brand">
      <div class="wordmark">KESTREL VENTURES</div>
      <div class="website">www.kestrelventures.com.au</div>
    </div>
  </section>

  <section class="card card-back" aria-label="Card back">
    <div class="wordmark">KESTREL VENTURES</div>
    <div class="contact">
      <div class="person-name">Liam Forde</div>
      <div class="person-role">Director</div>
      <div class="address">22 Carrow St Lindfield NSW 2070</div>
      <div class="contact-line">
        <svg viewBox="0 0 24 24" aria-hidden="true"><path d="M6.6 10.8a15 15 0 0 0 6.6 6.6l2.2-2.2a1 1 0 0 1 1-.25 11.4 11.4 0 0 0 3.6.57 1 1 0 0 1 1 1V20a1 1 0 0 1-1 1A17 17 0 0 1 3 4a1 1 0 0 1 1-1h3.5a1 1 0 0 1 1 1c0 1.25.2 2.45.57 3.57a1 1 0 0 1-.25 1z"/></svg>
        <span>0400 555 017</span>
      </div>
      <div class="contact-line">
        <svg viewBox="0 0 24 24" aria-hidden="true"><path d="M3 5h18v14H3z M3 5l9 7 9-7" fill="none" stroke="currentColor"/><rect x="3" y="5" width="18" height="14" rx="1"/><path d="M3 6l9 7 9-7" stroke="#6a6a6a" stroke-width="2" fill="none"/></svg>
        <span>liam@kestrelventures.com.au</span>
      </div>
      <div class="contact-line">
        <svg viewBox="0 0 24 24" aria-hidden="true"><circle cx="12" cy="12" r="10"/><path d="M2 12h20M12 2c3 3 3 17 0 20M12 2c-3 3-3 17 0 20" stroke="#6a6a6a" stroke-width="1.6" fill="none"/></svg>
        <span>www.kestrelventures.com.au</span>
      </div>
    </div>
  </section>
</main>
</body>
</html>
```